Design a (20.4 x 10.14) Banner that says - Keep Hope Rising From Harvest Crown TV Family

We want a design (20.4 x 10.14) with the words 'Keep Hope Rising' as the main text and 'From Harvest Crown TV Family' underneath. For 'Harvest Crown TV', we'd like you to use the logo which can be found in the image attached.

The image attached is just an example but please let your creative juices flow!

Target Market(s)

Christian

Industry/Entity Type

Christian

Requirements
Must have
• Must have the words 'Keep Hope Rising' and 'From Harvest Crown TV Family'.

```html
<!DOCTYPE html>
<html lang="en">
<head>
<meta charset="utf-8">
<title>Keep Hope Rising – Harvest Crown TV Family Banner</title>
<link rel="stylesheet" href="https://fonts.googleapis.com/css2?family=Poppins:wght@800&family=Montserrat:wght@500&display=swap">
<style>
  :root {
    --asphalt-dark: #6f6c6a;
    --asphalt-mid: #8e8a87;
    --asphalt-light: #b9b6b2;
    --stripe: #d9d7d3;
    --shadow: #3f4750;
    --pink-soft: #f68cb6;
    --pink-hot: #ec2a7c;
    --white: #ffffff;
    --badge: #2d3dd6;
  }
  * { margin: 0; padding: 0; box-sizing: border-box; }
  html, body {
    width: 1200px;
    height: 597px;
    overflow: hidden;
    background: var(--asphalt-mid);
  }
  .banner {
    position: relative;
    width: 1200px;
    height: 597px;
    overflow: hidden;
  }
  .banner__photo {
    position: absolute;
    inset: 0;
    background:
      radial-gradient(ellipse 70% 35% at 50% 12%, var(--stripe) 0%, transparent 70%),
      radial-gradient(ellipse 35% 60% at 15% 55%, var(--shadow) 0%, transparent 70%),
      radial-gradient(ellipse 35% 60% at 85% 55%, var(--shadow) 0%, transparent 70%),
      linear-gradient(180deg, var(--asphalt-light) 0%, var(--asphalt-mid) 45%, var(--asphalt-dark) 100%);
  }
  .headline {
    position: absolute;
    top: 30px;
    left: 0;
    width: 1200px;
    text-align: center;
    font-family: "Poppins", "Arial Black", sans-serif;
    font-weight: 800;
    font-size: 118px;
    line-height: 130px;
    letter-spacing: -2px;
  }
  .headline__line { display: block; color: var(--pink-soft); }
  .headline__line--accent { color: var(--pink-hot); }
  .signoff {
    position: absolute;
    left: 196px;
    top: 500px;
    font-family: "Montserrat", Arial, sans-serif;
    font-weight: 500;
    font-size: 25px;
    line-height: 30px;
    color: var(--white);
    text-transform: uppercase;
    white-space: nowrap;
  }
  .brand {
    position: absolute;
    left: 745px;
    top: 500px;
    display: flex;
    align-items: center;
    gap: 10px;
    font-family: "Montserrat", Arial, sans-serif;
    font-weight: 500;
    font-size: 20px;
    line-height: 30px;
    color: var(--white);
    text-transform: uppercase;
    white-space: nowrap;
  }
  .brand__mark {
    width: 26px;
    height: 26px;
    background: var(--badge);
  }
</style>
</head>
<body>
  <main class="banner">
    <div class="banner__photo" role="img" aria-label="Photograph of asphalt with white road markings and the mirrored shadows of a family holding hands"></div>

    <h1 class="headline">
      <span class="headline__line">Keep</span>
      <span class="headline__line headline__line--accent">Hope</span>
      <span class="headline__line">Rising</span>
    </h1>

    <p class="signoff">From Harvest Crown TV Family</p>

    <div class="brand">
      <span class="brand__mark" aria-hidden="true"></span>
      <span class="brand__name">Harvest Crown TV</span>
    </div>
  </main>
</body>
</html>
```